Tranquil Pathway Business Card

Logo attached. (will be printing onto thick white/off white textured card)

Double sided business card for two Therapists working at Tranquil Pathway.

Require one design, but with different name and mobile numbers on each card.

Target Market(s)

Medical, Health

Industry/Entity Type

Business

Contact Information for Business Card

Need one business card design, but a separate card for each person - Colin Marchetti and Marieke de Boeckx.

FRONT OF CARD

Logo

Name (Colin Marchetti on one card, Marieke de Boeckx on the other)
Professional Clinical Hypnotherapist

Consulting Rooms (Near Lindqvist Hospital)
482 Brackenfield Road
Dunmore VIC 3987

Colin@TranquilPathway.example.au OR Marieke@TranquilPathway.example.au

Mobile: 0455 872 604 (for Colin) OR
Mobile: 0467 290 518 (for Marieke)

BACK OF CARD

Logo

Website: www.TranquilPathway.example.au

Phone: 1300 958 471

Requirements
Must have
• Text and logo only. No additiional graphics.

```html
<!DOCTYPE html>
<html lang="en">
<head>
<meta charset="utf-8">
<title>Tranquil Pathway Business Card</title>
<link href="https://fonts.googleapis.com/css2?family=Jost:wght@400;500&display=swap" rel="stylesheet">
<style>
  :root {
    --ink-blue: #2b2fa3;
    --rule-grey: #6b6e70;
    --card-white: #fbfbf9;
    --backdrop: #e8e6e2;
  }
  * { margin: 0; padding: 0; box-sizing: border-box; }
  html, body { width: 1200px; height: 800px; overflow: hidden; }
  body {
    background: var(--backdrop);
    font-family: "Jost", sans-serif;
    color: var(--ink-blue);
    display: flex;
    align-items: center;
    justify-content: center;
    gap: 40px;
  }
  .card {
    width: 540px;
    height: 309px;
    background: var(--card-white);
    box-shadow: 0 6px 18px rgba(0,0,0,0.12);
    position: relative;
  }
  .brand-name {
    font-weight: 500;
    font-size: 20px;
    line-height: 1.2;
    letter-spacing: 0.02em;
    white-space: nowrap;
    color: var(--ink-blue);
  }
  /* front side */
  .card-front .brand-name {
    position: absolute;
    left: 0;
    width: 244px;
    text-align: center;
    top: 136px;
  }
  .card-front .divider {
    position: absolute;
    left: 244px;
    top: 70px;
    width: 1px;
    height: 178px;
    background: var(--rule-grey);
  }
  .card-front .details {
    position: absolute;
    right: 22px;
    top: 92px;
    text-align: right;
    font-size: 13.5px;
    line-height: 1.4;
    white-space: nowrap;
  }
  .person-name { font-size: 19px; font-weight: 400; line-height: 1.2; }
  .person-role { font-size: 14px; margin-bottom: 18px; }
  /* back side */
  .card-back {
    display: flex;
    flex-direction: column;
    align-items: center;
    justify-content: center;
    gap: 40px;
  }
  .card-back .brand-name { font-size: 22px; }
  .card-back .contact {
    text-align: center;
    font-size: 16px;
    line-height: 1.6;
  }
</style>
</head>
<body>
  <section class="card card-back" aria-label="Back of card">
    <p class="brand-name">Tranquil Pathway</p>
    <div class="contact">
      <p class="website">www.TranquilPathway.example.au</p>
      <p class="phone">1300 958 471</p>
    </div>
  </section>

  <section class="card card-front" aria-label="Front of card">
    <p class="brand-name">Tranquil Pathway</p>
    <div class="divider"></div>
    <div class="details">
      <p class="person-name">Colin Marchetti</p>
      <p class="person-role">Professional Clinical Hypnotherapist</p>
      <p>Consulting Rooms (Near Lindqvist Hospital)</p>
      <p>482 Brackenfield Road</p>
      <p>Dunmore VIC 3987</p>
      <p>Colin@TranquilPathway.example.au</p>
      <p>Mobile: 0455 872 604</p>
    </div>
  </section>
</body>
</html>
```